Car wellness, we make cars new and shiny

We need an design for a "small" ad that is published inside a magazine on a holiday tour bus. The audience is mostly 60+ years old.
We are a tinsmith's workshop and painter's shop company with a passion for shiny cars. We love to fix all the little scratches and dents a car gets over time and make it look new again.
The motto is car wellness (Wellness für Ihr Auto).
The ad has to be in German. If you are not fluent in German you may use the text in the example but feel free to use an appropriate font.
The COUPON is our call to action: We want the customer to call us. And it includes an offering of free get and return service of the customers car. It also inclueds some restrictions to the free service (proximity and valid until date).
Things that can't be changed are:
- the logo itself (the position, size and orientation are free)
- the color of the dot in the logo
- the size of the ad: 82mm x 118mm
- the magazines size: approx. A4
We expect a print ready result and would like to receive the files in original file format (eps, svg ...).
We hope for an eye-catching ad that drives the attention of the reader.
Car owners, with 60+ years of age.

```html
<!DOCTYPE html>
<html lang="de">
<head>
<meta charset="utf-8">
<title>Wellness für Ihr Auto – Anzeige</title>
<link rel="stylesheet" href="https://fonts.googleapis.com/css2?family=Anton&family=Roboto+Condensed:wght@400;700;900&display=swap">
<style>
  :root {
    --orange: #ef5a2a;
    --ink: #1b1b1b;
    --paper: #ffffff;
    --backdrop: #e9e4e0;
    --photo-dark: #2a2c30;
    --photo-warm: #c9861f;
  }
  * { box-sizing: border-box; margin: 0; padding: 0; }
  html, body {
    width: 1200px; height: 750px; overflow: hidden;
    background: var(--backdrop);
  }
  body { display: flex; align-items: center; justify-content: center; }

  .ad {
    position: relative;
    width: 486px; height: 700px;
    background: var(--paper);
    border: 11px dotted var(--orange);
    font-family: "Roboto Condensed", sans-serif;
    color: var(--ink);
    overflow: hidden;
  }

  .brand {
    position: absolute; top: 20px; left: 0; right: 0;
    display: flex; align-items: center; justify-content: center; gap: 8px;
    font-weight: 900; font-size: 30px; letter-spacing: 0.2px;
    color: var(--ink);
  }
  .brand-dot { width: 12px; height: 12px; border-radius: 50%; background: var(--orange); }

  .hero { position: absolute; top: 72px; left: 0; right: 0; height: 190px; }
  .hero-photo {
    position: absolute; top: 0; right: 0; width: 300px; height: 190px;
    background: linear-gradient(160deg, var(--photo-dark) 0%, #4a4a4e 45%, var(--photo-warm) 70%, var(--photo-dark) 100%);
  }
  .hero-band {
    position: absolute; top: 0; left: 0; width: 260px; height: 190px;
    background: var(--orange);
    clip-path: polygon(0 0, 100% 0, 60% 100%, 0 100%);
  }
  .hero-title {
    position: absolute; top: 26px; left: 22px;
    font-family: "Anton", sans-serif; font-size: 40px; font-weight: 400; line-height: 1.05;
    color: var(--paper);
  }

  .pitch {
    position: absolute; top: 286px; left: 24px; right: 24px;
    text-align: center; font-weight: 700; font-size: 27px; line-height: 1.18;
  }

  .cut-line {
    position: absolute; top: 420px; left: 0; right: 0;
    border-top: 2px dashed var(--ink);
  }
  .scissors { position: absolute; top: 404px; left: 10px; width: 34px; height: 34px; }

  .coupon {
    position: absolute; top: 440px; left: 22px; right: 22px; height: 210px;
    background: var(--orange);
    border: 3px dashed var(--ink);
    padding: 14px 16px;
    text-align: center;
  }
  .coupon-title { font-family: "Anton", sans-serif; font-size: 44px; font-weight: 400; line-height: 1; color: var(--ink); }
  .coupon-offer { margin-top: 6px; font-size: 16px; color: var(--paper); }
  .coupon-phone { margin-top: 4px; font-family: "Anton", sans-serif; font-size: 42px; line-height: 1.1; color: var(--ink); }
  .coupon-terms { margin-top: 6px; font-size: 14px; color: var(--ink); }
  .coupon-code { margin-top: 4px; font-size: 14px; font-weight: 700; color: var(--ink); text-align: right; }
</style>
</head>
<body>
  <article class="ad">
    <div class="brand"><span class="brand-name">carrosserie-talmatt.ch</span><span class="brand-dot"></span></div>

    <section class="hero">
      <div class="hero-photo" role="img" aria-label="Foto eines glänzenden orangen SUV in einer Werkstatt"></div>
      <div class="hero-band"></div>
      <h1 class="hero-title">Wellness<br>für Ihr<br>Auto</h1>
    </section>

    <p class="pitch">Ob kleinere Kratzer und Beulen oder ein grosseres Malheur, wir verhelfen Ihrem Auto zu neuem Glanz!</p>

    <div class="cut-line"></div>
    <svg class="scissors" viewBox="0 0 34 34" aria-hidden="true">
      <rect x="0" y="0" width="34" height="34" fill="var(--paper)"/>
      <circle cx="8" cy="8" r="5" fill="none" stroke="var(--ink)" stroke-width="3"/>
      <circle cx="8" cy="26" r="5" fill="none" stroke="var(--ink)" stroke-width="3"/>
      <line x1="12" y1="11" x2="32" y2="24" stroke="var(--ink)" stroke-width="3" stroke-linecap="round"/>
      <line x1="12" y1="23" x2="32" y2="10" stroke="var(--ink)" stroke-width="3" stroke-linecap="round"/>
    </svg>

    <section class="coupon">
      <h2 class="coupon-title">COUPON</h2>
      <p class="coupon-offer">Gratis Hol- &amp; Bring-Service Rufen Sie uns an:</p>
      <p class="coupon-phone">Tel: +41 56 000 12 34</p>
      <p class="coupon-terms">Gültig im Umkreis von 50Km um Talmatt bis am 31. Dez. 2021</p>
      <p class="coupon-code">CODE: Kiesbach</p>
    </section>
  </article>
</body>
</html>
```